Bright Polish Leaflet Campaign

We require an eye catching double sided leaflet which is for residential properties as a marketing tool to gain more business.
If you look at our website www.brightpolishteam.example then it may help you with more information of what we are about.

We require one side of the leaflet for our (Domestic Cleaning) Services, then the other side of the leaflet for our (Carpet and Upholstery Cleaning) Service.

The Domestic Cleaning Service Side: The services we offer are weekly, fortnightly, monthly. One Off Deep Cleans. Holiday cover provided. We also have a comprehensive insurance. You may want to use our company bullet point provided in pdf which will make it stand out and outline what we do e.g.:
-Weekly, fortnightly and Monthly Cleaning Service
-Deep Blitz Cleaning
-Covered by a Comprehensive Insurance
-Carpet and Upholstery Cleaning (see overleaf)

The Carpet and Upholstery Cleaning on the other side of the leaflet has to be eye catching!

Again use bullet points along the lines of:
-Stain Removal Specialists
-Quick Drying Time
-Fresh Deodorising Finish
-Eco Friendly

Both sides of the leaflet need a call to action eg. Call Today! Our company Telephone number which should be on the leaflet in bold is 01632 960 718 .The company email which should aslo be on there is info@brightpolishco.example and the website which is not live yet is www.brightpolishco.example. If you would like to add our company accreditations they are on the website and I have attached them also.

Target Market(s)

Domestic Households- Middle aged people In York United Kingdom

Industry/Entity Type

House Cleaning

Font styles to use
Serif
Sans Serif

Requirements
Must have
• -1 Side about Domestic Cleaning Services
• -1 Side about Carpet and Upholstery Cleaning
• -Bullet points with key points
• -Phone number/website/email address
• -Logo
Nice to have
• -BE CREATIVE, USE YOUR IMAGINATION AND CREATE EYE CATCHING MATERIAL.
• -Nice to have a background colour which goes nicely with the logo our company.
Should not have
• -Not to have pink in the leaflet or yellow as it doesn't show up well I don't believe. Up to the designer as I like to give you freedom to create something amazing.

```html
<!DOCTYPE html>
<html lang="en">
<head>
<meta charset="utf-8">
<title>Bright Polish – Domestic Cleaning Leaflet</title>
<link href="https://fonts.googleapis.com/css2?family=Open+Sans:ital,wght@0,400;0,600;0,700;0,800;1,600;1,700&display=swap" rel="stylesheet">
<style>
  :root {
    --brand-blue: #1fa6dc;
    --brand-grey: #9a9c9f;
    --ink: #161616;
    --panel-dark: #3a3b3d;
    --page-bg: #1e1e1e;
    --paper: #ffffff;
  }
  * { margin: 0; padding: 0; box-sizing: border-box; }
  html, body { width: 1200px; height: 1200px; overflow: hidden; background: var(--page-bg); }
  body { font-family: "Open Sans", Arial, sans-serif; position: relative; }

  .leaflet {
    position: absolute; left: 188px; top: 16px;
    width: 824px; height: 1167px;
    background: var(--paper); overflow: hidden;
  }
  .leaflet-shapes { position: absolute; inset: 0; }

  .brand {
    position: absolute; left: 52px; top: 78px;
    display: flex; align-items: center; gap: 10px;
  }
  .brand-dot { width: 20px; height: 20px; border-radius: 50%; background: var(--brand-grey); }
  .brand-name { font-size: 36px; font-weight: 800; color: var(--brand-blue); letter-spacing: -0.5px; }

  .headline { position: absolute; left: 372px; top: 38px; width: 440px; }
  .headline-main { font-size: 48px; font-weight: 700; color: var(--ink); line-height: 1; letter-spacing: -0.5px; }
  .headline-sub { font-size: 19px; font-weight: 700; color: var(--ink); margin-top: 6px; white-space: nowrap; }
  .headline-tag { font-size: 22px; font-style: italic; font-weight: 600; color: var(--brand-blue); margin-top: 4px; white-space: nowrap; margin-left: -3px; }

  .service-title { position: absolute; left: 246px; top: 722px; width: 544px; }
  .service-title-main { font-size: 51px; font-weight: 700; line-height: 1; white-space: nowrap; color: var(--ink); letter-spacing: -0.5px; }
  .service-title-main span { color: var(--brand-blue); }
  .service-title-sub {
    display: flex; align-items: center; gap: 10px; margin-top: 4px;
    font-size: 17px; font-weight: 600; color: var(--brand-grey); letter-spacing: 14px;
  }
  .service-title-sub::before, .service-title-sub::after { content: ""; flex: 1; height: 1px; background: #bbb; }
  .service-title-sub::after { margin-left: -14px; }

  .service-list { position: absolute; left: 348px; top: 822px; width: 470px; list-style: none; }
  .service-list li {
    position: relative; padding-left: 45px;
    font-size: 19.5px; font-style: italic; font-weight: 600; line-height: 30.4px; color: var(--ink);
  }
  .service-list li svg { position: absolute; left: 0; top: 5px; width: 34px; height: 24px; }

  .payments { position: absolute; left: 392px; top: 976px; }
  .payments-label { font-size: 6.5px; font-weight: 700; color: var(--ink); letter-spacing: 0.4px; }
  .payment-cards { display: flex; gap: 6px; margin-top: 3px; }
  .payment-card {
    width: 64px; height: 42px; border: 1px solid #555; background: #f3f3f3;
    display: flex; align-items: center; justify-content: center;
    font-size: 11px; font-weight: 700; color: var(--panel-dark);
  }

  .cta { position: absolute; left: 268px; top: 1084px; width: 530px; color: var(--paper); }
  .cta-line { font-size: 38px; font-weight: 700; white-space: nowrap; letter-spacing: -0.3px; line-height: 1.2; }
  .cta-line span { color: var(--brand-blue); }
  .cta-contact { font-size: 14px; margin-top: 6px; white-space: nowrap; }
  .cta-contact span { color: var(--brand-blue); }
  .cta-contact .sep { color: var(--paper); margin: 0 16px; }
</style>
</head>
<body>
<div class="leaflet">
  <svg class="leaflet-shapes" viewBox="0 0 824 1167" width="824" height="1167">
    <defs>
      <linearGradient id="teamPhotoTone" x1="0" y1="0" x2="1" y2="1">
        <stop offset="0" stop-color="#b8b8b8"/>
        <stop offset="0.5" stop-color="#e6e6e6"/>
        <stop offset="1" stop-color="#a9a9a9"/>
      </linearGradient>
      <linearGradient id="cleanerPhotoTone" x1="0" y1="0" x2="0" y2="1">
        <stop offset="0" stop-color="#e9eef6"/>
        <stop offset="0.45" stop-color="#4a6fc4"/>
        <stop offset="1" stop-color="#2f57b5"/>
      </linearGradient>
    </defs>
    <path d="M0,258 C250,165 600,145 824,282 L824,300 C600,185 250,205 0,276 Z" fill="var(--brand-blue)"/>
    <path d="M0,276 C250,205 600,185 824,300 L824,352 C600,215 250,228 0,300 Z" fill="var(--brand-grey)"/>
    <path role="img" aria-label="Photo of cleaners at work in a bright kitchen and living room" d="M0,300 C250,228 600,215 824,352 L824,540 C650,640 300,650 0,465 Z" fill="url(#teamPhotoTone)"/>
    <path d="M0,465 C300,650 650,640 824,540 L824,560 C650,668 300,672 0,500 Z" fill="var(--brand-blue)"/>
    <path d="M0,500 C300,672 650,668 824,560 L824,575 C650,700 300,700 0,548 Z" fill="var(--brand-grey)"/>
    <circle cx="612" cy="622" r="52" fill="#fff"/>
    <circle cx="612" cy="622" r="40" fill="none" stroke="var(--brand-grey)" stroke-width="3"/>
    <circle cx="732" cy="597" r="54" fill="#fff"/>
    <circle cx="732" cy="597" r="46" fill="none" stroke="#2a3f8f" stroke-width="4"/>
    <path d="M0,955 C40,1000 90,1030 150,1048 L0,1060 Z" fill="var(--brand-blue)"/>
    <path d="M0,1050 C300,1065 600,1040 824,990 L824,1000 C600,1052 300,1076 0,1066 Z" fill="var(--brand-blue)"/>
    <path d="M0,1066 C300,1076 600,1052 824,1000 L824,1167 L0,1167 Z" fill="var(--panel-dark)"/>
    <rect role="img" aria-label="Photo of a smiling cleaner holding a mop and a bucket of supplies" x="36" y="684" width="196" height="483" rx="6" fill="url(#cleanerPhotoTone)"/>
  </svg>

  <div class="brand">
    <span class="brand-dot"></span>
    <span class="brand-name">Bright Polish</span>
  </div>

  <header class="headline">
    <h1 class="headline-main">YORK’S FRESHEST</h1>
    <p class="headline-sub">&amp; MOST AFFORDABLE CLEANING SERVICE</p>
    <p class="headline-tag">Enjoy a Clean Home at an affordable price</p>
  </header>

  <div class="service-title">
    <h2 class="service-title-main">DOMESTIC <span>CLEANING</span></h2>
    <p class="service-title-sub">SERVICES</p>
  </div>

  <ul class="service-list">
    <li><svg viewBox="0 0 34 24"><path d="M3,13 L11,21 L31,3" fill="none" stroke="var(--brand-blue)" stroke-width="3" stroke-linecap="round"/></svg>Weekly, fortnightly and Monthly Cleaning Service</li>
    <li><svg viewBox="0 0 34 24"><path d="M3,13 L11,21 L31,3" fill="none" stroke="var(--brand-blue)" stroke-width="3" stroke-linecap="round"/></svg>Deep Blitz Cleaning</li>
    <li><svg viewBox="0 0 34 24"><path d="M3,13 L11,21 L31,3" fill="none" stroke="var(--brand-blue)" stroke-width="3" stroke-linecap="round"/></svg>Covered by a Comprehensive Insurance</li>
    <li><svg viewBox="0 0 34 24"><path d="M3,13 L11,21 L31,3" fill="none" stroke="var(--brand-blue)" stroke-width="3" stroke-linecap="round"/></svg>Carpet and Upholstery Cleaning (see overleaf)</li>
  </ul>

  <div class="payments">
    <p class="payments-label">WE ACCEPT THESE MAJOR CREDIT CARDS</p>
    <div class="payment-cards">
      <div class="payment-card">PayCard</div>
      <div class="payment-card">CardPlus</div>
    </div>
  </div>

  <footer class="cta">
    <p class="cta-line">CALL <span>01632 960 718</span> TODAY!!</p>
    <p class="cta-contact">Email: <span>info@brightpolishco.example</span><b class="sep">|</b>web: <span>www.brightpolishco.example</span></p>
  </footer>
</div>
</body>
</html>
```